Business cards for KORU Real Estate Holdings LLC

We need a cool, original business card design for a company based in the Washington DC metropolitan area. We are a new energetic and passionate Real Estate Investing Company that invests in all types of real estate; commercial, residential, industrial etc.

Our company color is Red since it reflects action, energy and speed; it is assertive confident, energizing, exciting, powerful, passionate and determined. So we would like business card communicate those qualities to the audience.

Our audiences are investors that want to invest with us, real estate sellers, buyers, and tenants who lease from us.

Our logo is attached

```html
<!DOCTYPE html>
<html lang="en">
<head>
<meta charset="utf-8">
<title>KORU Real Estate Holdings LLC — Business Cards</title>
<link rel="stylesheet" href="https://fonts.googleapis.com/css2?family=Open+Sans:wght@400;600;700&display=swap">
<style>
  :root {
    --red: #e01f26;
    --red-deep: #c8161d;
    --charcoal: #3a3b3d;
    --grey: #9c9ea1;
    --paper: #f4f4f4;
    --backdrop: #d3d5d8;
    --white: #ffffff;
  }
  * { margin: 0; padding: 0; box-sizing: border-box; }
  html, body {
    width: 1200px; height: 900px; overflow: hidden;
    background: var(--backdrop);
    font-family: "Open Sans", Arial, sans-serif;
  }
  .canvas { position: relative; width: 1200px; height: 900px; }
  .card {
    position: absolute; width: 520px; height: 300px;
    border-radius: 26px; overflow: hidden;
    background: var(--paper);
    box-shadow: 0 10px 28px rgba(0,0,0,.18);
  }
  .card-front { left: 53px; top: 300px; }
  .card-back  { left: 627px; top: 300px; }
  .card-bands { position: absolute; inset: 0; }

  .brand { position: absolute; display: flex; align-items: center; gap: 14px; }
  .brand-dot { flex: none; border-radius: 50%; background: var(--charcoal); }
  .brand-name { color: var(--red); font-weight: 700; line-height: 1.1; }

  /* front */
  .card-front .brand { left: 60px; top: 62px; }
  .card-front .brand-dot { width: 56px; height: 56px; }
  .card-front .brand-name { font-size: 30px; width: 320px; }
  .front-web {
    position: absolute; right: 40px; top: 212px;
    color: var(--white); font-size: 12px; letter-spacing: 6px;
  }

  /* back */
  .card-back .brand { left: 34px; top: 66px; }
  .card-back .brand-dot { width: 34px; height: 34px; }
  .card-back .brand-name { font-size: 18px; width: 200px; }
  .holder { position: absolute; right: 34px; top: 32px; text-align: right; }
  .holder-name { color: var(--red); font-weight: 700; font-size: 18px; letter-spacing: .5px; }
  .holder-title { color: var(--charcoal); font-size: 11px; }

  .contact { position: absolute; list-style: none; color: var(--white); font-size: 12.5px; white-space: nowrap; }
  .contact li { display: flex; align-items: center; gap: 9px; margin-bottom: 10px; }
  .contact svg { flex: none; }
  .contact-phone { left: 186px; top: 172px; }
  .contact-web { left: 330px; top: 172px; }
  .contact-address { left: 34px; top: 232px; }
  .contact-address li { align-items: flex-start; line-height: 1.55; }
</style>
</head>
<body>
<main class="canvas">

  <section class="card card-front" aria-label="Business card front">
    <svg class="card-bands" viewBox="0 0 520 300" width="520" height="300" aria-hidden="true">
      <rect x="0" y="0" width="520" height="300" fill="var(--paper)"/>
      <rect x="0" y="182" width="520" height="2.5" fill="var(--red)"/>
      <rect x="0" y="196" width="520" height="104" fill="var(--red)"/>
      <rect x="0" y="286" width="520" height="14" fill="var(--red-deep)"/>
    </svg>
    <div class="brand">
      <span class="brand-dot"></span>
      <span class="brand-name">KORU Real Estate Holdings LLC</span>
    </div>
    <p class="front-web">www.koruholdings.com</p>
  </section>

  <section class="card card-back" aria-label="Business card back">
    <svg class="card-bands" viewBox="0 0 520 300" width="520" height="300" aria-hidden="true">
      <rect x="0" y="0" width="520" height="300" fill="var(--paper)"/>
      <rect x="0" y="138" width="520" height="8" fill="var(--charcoal)"/>
      <rect x="0" y="151" width="520" height="149" fill="var(--red)"/>
    </svg>

    <div class="brand">
      <span class="brand-dot"></span>
      <span class="brand-name">KORU Real Estate Holdings LLC</span>
    </div>

    <div class="holder">
      <p class="holder-name">ALEX MARLOW JR</p>
      <p class="holder-title">Your Job Title</p>
    </div>

    <ul class="contact contact-phone">
      <li>
        <svg width="18" height="18" viewBox="0 0 18 18" aria-hidden="true"><circle cx="9" cy="9" r="9" fill="var(--charcoal)"/><path d="M6 4.5l2 .3.6 2.2-1.2.9a6 6 0 0 0 2.7 2.7l.9-1.2 2.2.6.3 2A1.5 1.5 0 0 1 12 13.5 8 8 0 0 1 4.5 6 1.5 1.5 0 0 1 6 4.5z" fill="var(--white)"/></svg>
        +(000) 2468 1357
      </li>
      <li>
        <svg width="18" height="18" viewBox="0 0 18 18" aria-hidden="true"><circle cx="9" cy="9" r="9" fill="var(--charcoal)"/><rect x="6" y="4.5" width="6" height="3" fill="var(--white)"/><rect x="4.5" y="7.5" width="9" height="4" rx="1" fill="var(--white)"/><rect x="6" y="10.5" width="6" height="3" fill="var(--white)" stroke="var(--charcoal)" stroke-width=".6"/></svg>
        +(000) 2468 1358
      </li>
    </ul>

    <ul class="contact contact-web">
      <li>
        <svg width="18" height="18" viewBox="0 0 18 18" aria-hidden="true"><circle cx="9" cy="9" r="9" fill="var(--charcoal)"/><circle cx="9" cy="9" r="4.5" fill="none" stroke="var(--white)" stroke-width="1.2"/><path d="M4.5 9h9M9 4.5c-2 2.5-2 6.5 0 9M9 4.5c2 2.5 2 6.5 0 9" fill="none" stroke="var(--white)" stroke-width="1"/></svg>
        www.koruholdings.com
      </li>
      <li>
        <svg width="18" height="18" viewBox="0 0 18 18" aria-hidden="true"><circle cx="9" cy="9" r="9" fill="var(--charcoal)"/><rect x="4.5" y="6" width="9" height="6.5" fill="var(--white)"/><path d="M4.5 6l4.5 3.8L13.5 6" fill="none" stroke="var(--charcoal)" stroke-width="1"/></svg>
        alex@koruholdings.com
      </li>
    </ul>

    <ul class="contact contact-address">
      <li>
        <svg width="18" height="18" viewBox="0 0 18 18" aria-hidden="true"><circle cx="9" cy="9" r="9" fill="var(--charcoal)"/><path d="M9 4a3.3 3.3 0 0 1 3.3 3.3C12.3 10 9 14 9 14S5.7 10 5.7 7.3A3.3 3.3 0 0 1 9 4z" fill="var(--white)"/><circle cx="9" cy="7.3" r="1.2" fill="var(--charcoal)"/></svg>
        <span>1420 Brightwater Ave,<br>Falls Church VA 22041</span>
      </li>
    </ul>
  </section>

</main>
</body>
</html>
```